Lena Hartwell Web

Lena Hartwell is a singer/songwriter that has a presence in the market for over 20 years. She currently has a website, lenahartwell.example that needs a major makeover. IT needs to be reorganized to; 1) make it more user friendly; 2) enable multi-languages including; Spanish, French, Russian, Japanese, Chinese and Portuguese; 3) enable purchases online through a storefront of promotional merchandise and music tracks. She has a logo that needs an update, as well as we currently have a business card open on PixelBazaar for input. Working to re-brand, or refresh her brand.

Lena Hartwell is the next Rosa Delmont! She has 5 platinum records, Lumen Award nominations and tours with Harold Prescott globally and is Nora Vandermeer's key backup singer for 12 years.
Updates

Some common questions have come up.  Here is some further input:

1) Colors - No specific color in mind but probably earth tones.  Although at this point we''re completely open.  Mary likes classical style, Russian, French decor.  Paris architecture. Greek, Italian textures, Goddess like symbols from the Roman Empire, or the symbols and pomp of the British monarchy.  One name on tap for the new CD is "Lanterns Over Quiet Water"
2) Example website - I have not found a new one specifically, but what I don''t like about the existing one is it is not easy to navigate.  Needs to be streamlined and easy to navigate with a storefront for merchandise and music downloads.  
3) On Logo - We''re revamping a "Global" merchandise rollout logo.  We''ve also considered possibly modifying the old english "Hartwell" family crest which signifies royalty, but have not explored that too much.  The hexagon yellow logo on her current website, I was thinking of modifying to gold (brushed - or polished?), then taking the LH lettering using a fountain pen type look there the line thickness flows with pressure on the pen, then make the gold look like a pillow, with the letter making an impression into the gold pillow.  This expands to a high quality pin, blinged up broach with diamonds imbedded for example, Global label identity, tee shirts, label tag on fashion clothing etc etc. 
 4) One thing marketing has asked us to build is a routine video blog to reach out to fans in a personal way.  Short clips of daily activity, travel prep for shows, etc. Possibly a signup/fanpage where people get emails sent back whenever anything new is posted, like a video blog, new pics, new events.  A menu to choose what you get updates on. 

Thanks, Dennis

Target Market(s)

1) Fan base in Europe, Asia, Latin America and North America
2) Movie producers seeking soundtracks
3) Private clients seeking an outstanding performer for corporate events

Industry/Entity Type

Singer

Requirements
Must have
• Better organization into smaller pages. Items critical include: 1) music tracks, 2) ClipStream links, 3) photos & Video, 4) storefront to enable online merchandise purchase 5) a way to illustrate her genre from; gospel, to rock, funk, R&B, country,

```html
<!DOCTYPE html>
<html lang="en">
<head>
<meta charset="utf-8">
<title>Lena Hartwell – Event Details</title>
<link href="https://fonts.googleapis.com/css2?family=Open+Sans:wght@400;600;700&family=Oswald:wght@500;700&display=swap" rel="stylesheet">
<style>
:root{
  --bg-deep:#2a1405;
  --panel-dark:#3a1d07;
  --bar:#2f1605;
  --gold:#f7c21b;
  --orange:#f15a22;
  --white:#ffffff;
  --cream:#f3e6d2;
  --caption-dark:#5a3413;
}
*{margin:0;padding:0;box-sizing:border-box}
html,body{width:1200px;height:2474px;overflow:hidden}
body{position:relative;background:var(--bg-deep);font-family:"Open Sans",Arial,sans-serif;color:var(--white)}
.abs{position:absolute}
.crowd-backdrop{left:0;top:90px;width:1200px;height:1885px;background:radial-gradient(ellipse at 50% 40%,#5a2f0e 0%,#3b1d07 55%,#2a1405 100%)}

/* header */
.site-header{left:0;top:0;width:1200px;height:90px;background:var(--bar);border-bottom:3px solid #e9dccb}
.brand{left:148px;top:20px;display:flex;align-items:center;gap:10px}
.brand-square{width:34px;height:34px;background:var(--gold)}
.brand-name{font-weight:700;font-size:28px;color:var(--gold)}
.main-nav{top:31px;font-size:15px;color:var(--white);white-space:nowrap}
.main-nav.active{color:var(--gold)}

/* main panel */
.panel{left:161px;top:134px;width:876px;height:1804px;background:rgba(74,39,9,.55)}
.section-title{font-size:27px;font-weight:600;color:var(--white);white-space:nowrap}
.section-title span{color:var(--gold)}
.details-bar{left:161px;top:134px;width:876px;height:68px;background:var(--panel-dark);border-bottom:4px solid var(--gold)}
.details-bar .section-title{position:absolute;left:53px;top:15px}
.hero-photo{left:161px;top:206px;width:876px;height:406px;background:radial-gradient(ellipse at 70% 30%,#8a5a2a 0%,#5a3210 45%,#3a1e07 100%)}
.hero-name{left:324px;top:242px;font-size:36px;font-weight:600;white-space:nowrap}
.count{width:115px;height:115px;border:4px solid var(--gold);border-radius:50%;text-align:center;top:330px}
.count b{display:block;font-family:"Oswald",sans-serif;font-weight:500;font-size:38px;color:var(--gold);line-height:1;margin-top:22px}
.count small{font-size:14px;text-transform:uppercase;color:var(--cream)}
.soul{left:324px;top:474px;font-family:"Oswald",sans-serif;font-weight:700;color:var(--gold);line-height:.95;white-space:nowrap}
.soul .l1{font-size:32px;font-weight:500;letter-spacing:1px}
.soul .l2{font-size:44px}
.hero-copy{left:538px;top:478px;width:412px;font-size:11.5px;line-height:19px;color:var(--cream);text-align:justify}

/* event info */
.info-title{left:214px;top:632px}
.info-copy{left:214px;top:678px;width:760px;font-size:11.5px;line-height:19px;color:var(--cream)}
.arrow-btn{top:753px;width:18px;height:20px;background:#6b4218}
.card{top:796px;width:244px;height:334px}
.card-photo{left:0;top:0;width:244px;height:272px}
.card-caption{left:0;top:272px;width:244px;height:62px;text-align:center;padding-top:8px}
.card-caption h3{font-size:17px;font-weight:600}
.card-caption p{font-size:13px}
.card.featured{outline:3px solid var(--gold)}
.card.featured .card-caption{background:var(--gold);color:#3a1d07}
.card.dim .card-caption{background:var(--caption-dark);color:#8c6b49}
.card.dim .card-photo{opacity:.75}
.share-dot{width:34px;height:34px;border-radius:50%;background:var(--white);top:198px}

/* event dates */
.dates-band{left:161px;top:1180px;width:876px;height:315px;background:radial-gradient(ellipse at 45% 70%,#6a3c12 0%,#4a2709 60%,#3b1e07 100%)}
.dates-title{left:214px;top:1203px}
.date-row{left:214px;width:760px;height:40px}
.day{left:0;top:0;font-size:30px;color:var(--gold);line-height:40px;width:40px}
.day-sep{left:42px;top:6px;width:2px;height:30px;background:var(--gold)}
.day-meta{left:52px;top:5px;font-size:11px;line-height:14px;color:var(--gold);white-space:nowrap}
.city,.venue{top:9px;font-size:17px;color:var(--gold);white-space:nowrap}
.btn{top:8px;height:24px;font-size:10px;font-weight:700;line-height:24px;text-align:center;text-transform:uppercase;white-space:nowrap}
.btn-info{left:590px;width:79px;background:var(--white);color:#3a1d07}
.btn-ticket{left:675px;width:74px;background:var(--orange);color:var(--white)}

/* tickets */
.tickets-title{left:214px;top:1524px}
.ticket{top:1580px;background:var(--white);border:3px solid var(--gold);text-align:center;color:#3a1d07}
.ticket-head{height:74px;padding-top:8px;font-size:27px;line-height:29px}
.ticket-head small{display:block;font-size:17px}
.ticket-price{height:57px;background:var(--panel-dark);color:var(--gold);font-size:34px;line-height:57px}
.ticket-perks{padding-top:12px;font-size:12.5px;line-height:20px;font-weight:600;text-transform:uppercase}
.ticket-perks .hot{color:var(--orange)}
.ticket-buy{display:inline-block;margin-top:10px;background:var(--orange);color:var(--white);font-size:14px;font-weight:700;padding:8px 16px;text-transform:uppercase}
.ticket.vip{background:var(--gold);border-color:#fff3b0}
.ticket.vip .ticket-head{background:var(--gold);font-size:34px}
.ticket.vip .ticket-price{background:var(--white);color:var(--gold);font-size:38px}

/* footer */
.footer-nav-band{left:0;top:1975px;width:1200px;height:62px;background:var(--bar)}
.social-sq{top:1992px;width:29px;height:29px;background:#5a3513}
.foot-link{top:1996px;font-size:12.5px;color:var(--white)}
.footer-body{left:0;top:2037px;width:1200px;height:375px;background:#2c1505}
.news-title{left:534px;top:2086px;font-size:26px}
.news-input{left:691px;top:2091px;width:202px;height:26px;background:var(--white);color:#555;font-size:11px;padding:5px 8px}
.news-btn{left:901px;top:2091px;width:74px;height:26px;background:var(--gold);color:#3a1d07;font-size:11px;text-align:center;line-height:26px}
.foot-head{top:2203px;font-size:18px;font-weight:600}
.thumb{width:77px;height:59px}
.tweet{left:460px;top:2236px;width:220px}
.tweet .who{color:var(--gold);font-size:15px}
.tweet .where{font-size:14px;line-height:20px;margin-top:6px}
.tweet .body{font-size:10px;line-height:14px;margin-top:10px;color:var(--cream)}
.tweet .stamp{font-size:9px;color:var(--orange);margin-top:6px}
.tweet-dot{left:625px;top:2236px;width:22px;height:22px;border-radius:50%;background:var(--white)}
.video-row{left:758px;width:285px;height:40px}
.video-thumb{left:0;top:0;width:56px;height:37px}
.video-text{left:75px;top:0;width:200px;font-size:9.5px;line-height:13px;color:var(--cream)}
.copyright-band{left:0;top:2412px;width:1200px;height:62px;background:var(--bar);text-align:center;font-size:11px;color:var(--gold);line-height:62px}
</style>
</head>
<body>

<div class="abs crowd-backdrop" role="img" aria-label="Concert crowd with raised hands, toned in warm sepia"></div>

<header class="abs site-header">
  <div class="abs brand"><div class="brand-square"></div><div class="brand-name">LH</div></div>
  <nav>
    <span class="abs main-nav active" style="left:542px">Home</span>
    <span class="abs main-nav" style="left:612px">Explore</span>
    <span class="abs main-nav" style="left:695px">Event</span>
    <span class="abs main-nav" style="left:765px">Album</span>
    <span class="abs main-nav" style="left:845px">Blog</span>
    <span class="abs main-nav" style="left:922px">Price</span>
    <span class="abs main-nav" style="left:983px">Contacts</span>
  </nav>
</header>

<main>
  <div class="abs panel"></div>

  <section>
    <div class="abs details-bar"><h2 class="section-title">Event <span>Details</span></h2></div>
    <div class="abs hero-photo" role="img" aria-label="Lena Hartwell singing on stage under warm spotlights"></div>
    <h1 class="abs hero-name">Lena Hartwell</h1>
    <div class="abs count" style="left:316px"><b>200</b><small>Days</small></div>
    <div class="abs count" style="left:467px"><b>03</b><small>Hours</small></div>
    <div class="abs count" style="left:615px"><b>10</b><small>Minuties</small></div>
    <div class="abs count" style="left:765px"><b>45</b><small>Seconds</small></div>
    <div class="abs soul"><div class="l1">THE SOUL</div><div class="l2">OF MUSIC</div></div>
    <p class="abs hero-copy">With a powerfully unique voice and a definitive sound, Lena Hartwell consistently delivers soul stirring performances that captivate audiences around the world. Using her past as a spring board, Lena channels memories into melodies that are proud and strong.</p>
  </section>

  <section>
    <h2 class="abs section-title info-title">Event <span>Info</span></h2>
    <p class="abs info-copy">Lorem ipsum dolor sit amet, consectetur adipiscing elit. Proin non rhoncus dolor. Curabitur rhoncus convallis erat, a placerat risus posuere and or vestibulum.With a powerfully unique voice and a definitive sound, Lena Hartwell consistently delivers soul stirring performances that captivate audiences around the world. Using her past as a spring board, Lena channels memories into melodies that are proud and strong.</p>
    <div class="abs arrow-btn" style="left:940px"><svg width="18" height="20"><path d="M11 6 L7 10 L11 14" stroke="#f7c21b" stroke-width="2" fill="none"/></svg></div>
    <div class="abs arrow-btn" style="left:962px"><svg width="18" height="20"><path d="M7 6 L11 10 L7 14" stroke="#f7c21b" stroke-width="2" fill="none"/></svg></div>

    <article class="abs card featured" style="left:214px">
      <div class="abs card-photo" role="img" aria-label="Lena Hartwell singing into a microphone" style="background:linear-gradient(160deg,#b07a3a,#6a3a12)"></div>
      <svg class="abs" style="left:98px;top:110px" width="48" height="48"><circle cx="24" cy="24" r="22" fill="#fff" opacity=".85"/><circle cx="21" cy="21" r="8" stroke="#3a1d07" stroke-width="3" fill="none"/><line x1="27" y1="27" x2="34" y2="34" stroke="#3a1d07" stroke-width="3"/></svg>
      <div class="abs share-dot" style="left:54px" aria-label="Facelink"></div>
      <div class="abs share-dot" style="left:105px;top:188px;background:var(--gold)" aria-label="Chirpline"></div>
      <div class="abs share-dot" style="left:156px" aria-label="Workweb"></div>
      <div class="abs card-caption"><h3>Lena Hartwell</h3><p>We Can Get There</p></div>
    </article>
    <article class="abs card dim" style="left:476px">
      <div class="abs card-photo" role="img" aria-label="Lena Hartwell performing on a concert stage" style="background:linear-gradient(160deg,#7a5030,#3e2210)"></div>
      <div class="abs card-caption"><h3>Lena Hartwell</h3><p>We Can Get There</p></div>
    </article>
    <article class="abs card dim" style="left:740px">
      <div class="abs card-photo" role="img" aria-label="Lena Hartwell on stage in a white gown at an anniversary show" style="background:linear-gradient(160deg,#6a4428,#2e180a)"></div>
      <div class="abs card-caption"><h3>Lena Hartwell</h3><p>We Can Get There</p></div>
    </article>
  </section>

  <section>
    <div class="abs dates-band" role="img" aria-label="Faded clock face in brown tones"></div>
    <h2 class="abs section-title dates-title">Event <span>Date</span></h2>

    <div class="abs date-row" style="top:1258px">
      <span class="abs day">12</span><span class="abs day-sep"></span>
      <span class="abs day-meta">May,2014<br>10:00PM</span>
      <span class="abs city" style="left:223px">PARIS,FR</span>
      <span class="abs venue" style="left:405px">LUMIÈRE HALL</span>
      <span class="abs btn btn-info">More Info</span><span class="abs btn btn-ticket">Buy Ticket</span>
    </div>
    <div class="abs date-row" style="top:1326px">
      <span class="abs day">22</span><span class="abs day-sep"></span>
      <span class="abs day-meta">May,2014<br>10:00PM</span>
      <span class="abs city" style="left:223px">SANTIAGO , CHILI</span>
      <span class="abs btn btn-info">More Info</span><span class="abs btn btn-ticket">Buy Ticket</span>
    </div>
    <div class="abs date-row" style="top:1394px">
      <span class="abs day">02</span><span class="abs day-sep"></span>
      <span class="abs day-meta">May,2014<br>10:00PM</span>
      <span class="abs city" style="left:223px">PARIS</span>
      <span class="abs venue" style="left:380px">USA</span>
      <span class="abs btn btn-info">More Info</span><span class="abs btn btn-ticket">Buy Ticket</span>
    </div>
  </section>

  <section>
    <h2 class="abs section-title tickets-title">Ticket <span>Price</span></h2>
    <div class="abs ticket" style="left:212px;width:151px;height:245px">
      <div class="ticket-head">REGULAR<small>ZONE</small></div>
      <div class="ticket-price">$100</div>
      <div class="ticket-perks">Free Seating<br>No Snacks</div>
      <span class="ticket-buy">Buy Ticket</span>
    </div>
    <div class="abs ticket" style="left:394px;width:175px;height:265px">
      <div class="ticket-head">CLASSIC<small>ZONE</small></div>
      <div class="ticket-price">$200</div>
      <div class="ticket-perks">Free Seating<br>No Snacks<br>Free Tshirt</div>
      <span class="ticket-buy">Buy Ticket</span>
    </div>
    <div class="abs ticket" style="left:606px;width:171px;height:286px">
      <div class="ticket-head">ROCK<small>ZONE</small></div>
      <div class="ticket-price">$800</div>
      <div class="ticket-perks">Numbered Seating<br>No Snacks<br><span class="hot">Free Tshirt &amp; Cap</span></div>
      <span class="ticket-buy">Buy Ticket</span>
    </div>
    <div class="abs ticket vip" style="left:812px;width:174px;height:311px">
      <div class="ticket-head" style="padding-top:10px;height:88px">VIP<small>ZONE</small></div>
      <div class="ticket-price">$1000</div>
      <div class="ticket-perks">Numbered Seating<br>No Snacks<br><span class="hot">Free Tshirt &amp; Cap</span></div>
      <span class="ticket-buy" style="font-size:16px;padding:10px 20px">Buy Ticket</span>
    </div>
  </section>
</main>

<footer>
  <div class="abs footer-nav-band"></div>
  <div class="abs social-sq" style="left:212px" aria-label="Callnest"></div>
  <div class="abs social-sq" style="left:256px" aria-label="Chirpline"></div>
  <div class="abs social-sq" style="left:300px" aria-label="Snapgrid"></div>
  <div class="abs social-sq" style="left:344px" aria-label="Facelink"></div>
  <div class="abs social-sq" style="left:388px" aria-label="Feedline"></div>
  <div class="abs social-sq" style="left:432px" aria-label="Workweb"></div>
  <div class="abs social-sq" style="left:476px" aria-label="Reelbox"></div>
  <nav>
    <span class="abs foot-link" style="left:585px;font-weight:700">Home</span>
    <span class="abs foot-link" style="left:653px">Event</span>
    <span class="abs foot-link" style="left:710px">Album</span>
    <span class="abs foot-link" style="left:773px">Blog</span>
    <span class="abs foot-link" style="left:826px">About</span>
    <span class="abs foot-link" style="left:889px">Price</span>
    <span class="abs foot-link" style="left:944px">Contact</span>
  </nav>

  <div class="abs footer-body"></div>
  <h3 class="abs news-title">Newsletter</h3>
  <div class="abs news-input">Enter your Email</div>
  <div class="abs news-btn">Subscribe</div>

  <h4 class="abs foot-head" style="left:212px">Gallery</h4>
  <div class="abs thumb" role="img" aria-label="Portrait of Lena Hartwell" style="left:212px;top:2243px;background:linear-gradient(135deg,#6a4a3a,#2a1a14)"></div>
  <div class="abs thumb" role="img" aria-label="Lena Hartwell in red stage light" style="left:294px;top:2243px;background:linear-gradient(135deg,#a02818,#3a0c08)"></div>
  <div class="abs thumb" role="img" aria-label="Lena Hartwell album cover shot" style="left:212px;top:2306px;background:linear-gradient(135deg,#4a4a6a,#1a1a2a)"></div>
  <div class="abs thumb" role="img" aria-label="Lena Hartwell close portrait" style="left:294px;top:2306px;background:linear-gradient(135deg,#7a5a48,#2e1e16)"></div>

  <h4 class="abs foot-head" style="left:460px">Latest Tweet</h4>
  <div class="abs tweet-dot"></div>
  <div class="abs tweet">
    <div class="who">With NoraVandermeer</div>
    <div class="where">Nora Vandermeer Crescent Hall<br>Atlantic City, NJ</div>
    <div class="body">In hac habitasse platea dictumst. Nam ulvinar, odio sed rhoncus suscipit</div>
    <div class="stamp">FRI, JAN 10, 2014 - 8:00 PM</div>
  </div>

  <h4 class="abs foot-head" style="left:763px">Latest Video</h4>
  <div class="abs video-row" style="top:2245px">
    <div class="abs video-thumb" role="img" aria-label="Video still of a performance" style="background:linear-gradient(135deg,#5a5a7a,#1e1e2e)"></div>
    <p class="abs video-text">Lorem ipsum dolor sit amet, and consectetur adipiscing elit. Nunc in felis arcu.</p>
  </div>
  <div class="abs video-row" style="top:2289px">
    <div class="abs video-thumb" role="img" aria-label="Video still of a stage show" style="background:linear-gradient(135deg,#4a5a8a,#1a1e34)"></div>
    <p class="abs video-text">Lorem ipsum dolor sit amet, and consectetur adipiscing elit. Nunc in felis arcu.</p>
  </div>
  <div class="abs video-row" style="top:2334px">
    <div class="abs video-thumb" role="img" aria-label="Video still under red lights" style="background:linear-gradient(135deg,#9a2010,#2e0a06)"></div>
    <p class="abs video-text">Lorem ipsum dolor sit amet, and consectetur adipiscing elit. Nunc in felis arcu.</p>
  </div>

  <div class="abs copyright-band">Copyright © 2014 - All Rights Reserved.</div>
</footer>

</body>
</html>
```